Design a WordPress website for a Wedding Company in Paradise

Seeking beautiful and creative WordPress website design for the Caribbean's leading small weddings and elopements firm. We have beautiful weddings (100+ a year), beautiful images, drone photos and videos, and much more, and we need a beautiful website to reflect that.

We like (not love) our current website, www.velmorabridalco.com. Much of the tabs and functionality can stay the same; however, we need a cleaner, crisper design that doesn't have glitches (yes, that's the responsibility of the coder in the future).

Featuring images and videos are very important. In addition, having a clean and elegant interface and aesthetic will allow the photos and imagery to shine.
Updates

Hi Designers, I'm so sorry but we haven't given this the attention it deserves, as our operations manager has been out of the office. We're pushing the deadline out a few days so that we can provide better and more detailed feedback for the submissions you've worked on, creating better results. Thank you for your patience!

Target Market(s)

Couples from the USA looking to travel to and get married in Puerto Rico, a beautiful Caribbean island.

Number of Pages Required

5+ page

Font styles to use
Other font styles liked:
• Fonts and colors are mostly provided in design guidelines. A versatile script font that's not too frilly might be useful as well.

Requirements
Must have
• -Clean and elegant web design. less is more.
-Utilize existing logo and colors
-Highlight photos and videos throughout
-Blog page design
-Video page design
-Photo gallery page design
-Landing page design for Trelvix Promoads campaigns
Should not have
• -lots of frills, hearts, palm trees, and stereotypical wedding and island imagery and themes

```html
<!DOCTYPE html>
<html lang="en">
<head>
<meta charset="utf-8">
<title>Services — Velmora Bridal Co.</title>
<link href="https://fonts.googleapis.com/css2?family=Gelasio:wght@400&family=Mulish:wght@400;700;800&family=Arimo:wght@700&display=swap" rel="stylesheet">
<style>
:root{
  --gold:#dcb877;
  --gold-text:#d5ab5f;
  --ink:#1e1e1e;
  --body:#4a4a4a;
  --white:#ffffff;
  --rule:#cfcfcf;
  --teal:#5fb5ad;
}
*{margin:0;padding:0;box-sizing:border-box}
html,body{width:1200px;height:3878px;overflow:hidden;background:var(--white)}
body{position:relative;font-family:"Mulish",sans-serif;color:var(--body)}
.abs{position:absolute}

/* header */
.nav-bar{left:0;top:125px;width:1200px;height:44px;background:var(--gold)}
.nav-link{top:125px;height:44px;line-height:44px;font-family:"Arimo",sans-serif;font-weight:700;font-size:17px;color:var(--white);letter-spacing:.3px;text-decoration:none}
.brand-dome{left:462px;top:0;width:276px;height:196px;background:var(--white);border-radius:0 0 138px 138px / 0 0 72px 72px}
.brand{left:462px;top:84px;width:276px;text-align:center;font-family:"Gelasio",serif;font-size:33px;color:var(--gold-text);letter-spacing:2px}
.brand-dot{left:586px;top:20px;width:28px;height:28px;border-radius:50%;background:var(--teal);opacity:.55}

/* photo areas */
.photo{left:0;width:1200px}
.hero{top:169px;height:512px;background:linear-gradient(120deg,#3f8a9c 0%,#6e8a55 35%,#8a8a4a 55%,#b9b7ad 80%,#5c6a42 100%)}
.hero-title{left:104px;top:308px;font-family:"Gelasio",serif;font-size:74px;color:var(--white);line-height:1}
.arrow{top:410px}

.service{left:0;width:1200px}
.s-elope{top:681px;height:554px;background:linear-gradient(90deg,#6a5a4a 0%,#c8935c 30%,#e9cfa9 48%,#f6f2ee 62%,#fbfbfb 100%)}
.s-beach{top:1235px;height:536px;background:linear-gradient(90deg,#f7f7f7 0%,#f1f1f1 40%,#b7c9d4 60%,#2b5f8a 78%,#224d78 100%)}
.s-beach-sand{left:0;top:1500px;width:1200px;height:271px;background:linear-gradient(90deg,rgba(255,255,255,0) 0%,rgba(255,255,255,0) 45%,rgba(221,205,180,.8) 65%,#d9c7a7 100%)}
.s-vow{top:1792px;height:552px;background:linear-gradient(90deg,#7b6b5a 0%,#a08a72 25%,#b3b6bf 42%,#eef0f2 60%,#ffffff 80%)}
.s-cruise{top:2344px;height:557px;background:linear-gradient(90deg,#ffffff 0%,#f7f9fa 38%,#9fb8c4 55%,#26618a 72%,#0f3f6b 100%)}
.s-extra{top:2901px;height:557px;background:linear-gradient(90deg,#8d8f4a 0%,#a9a36a 25%,#d6cfb8 45%,#f3f1ec 62%,#ffffff 80%)}

.heading{font-family:"Gelasio",serif;font-size:55px;color:var(--ink);line-height:1;font-weight:400}
.copy{font-size:15.5px;line-height:31px;color:var(--body);width:490px}
.btn{width:207px;height:57px;border:2px solid var(--ink);font-weight:800;font-size:17.5px;color:var(--ink);display:flex;align-items:center;justify-content:center;letter-spacing:.3px;text-decoration:none}

/* footer */
.foot-brand{left:100px;top:3622px;width:280px;text-align:center;font-family:"Gelasio",serif;font-size:36px;color:var(--gold-text);letter-spacing:2px}
.foot-dot{left:226px;top:3540px;width:30px;height:30px;border-radius:50%;background:var(--teal);opacity:.55}
.search{left:113px;top:3720px;width:297px;height:44px;border:1px solid #cfcfcf;display:flex}
.search-field{flex:1;position:relative}
.search-btn{width:89px;background:var(--gold);color:var(--white);font-family:"Arimo",sans-serif;font-weight:700;font-size:15px;display:flex;align-items:center;justify-content:center}
.foot-heading{font-family:"Gelasio",serif;font-size:24px;color:#333}
.foot-copy{font-size:13.5px;line-height:27.5px;color:#555;width:380px}
.contact-row{font-size:13.5px;color:#555;display:flex;align-items:center;gap:10px}
.rule{left:113px;top:3797px;width:977px;height:1px;background:var(--rule)}
.copyright{left:113px;top:3830px;font-size:15px;color:#444}
.social{top:3826px;width:24px;height:24px;border-radius:3px;background:var(--teal)}
</style>
</head>
<body>

<!-- header -->
<div class="abs nav-bar"></div>
<a class="abs nav-link" style="left:181px">PACKAGES</a>
<a class="abs nav-link" style="left:352px">ABOUT</a>
<a class="abs nav-link" style="left:795px">WEDDINGS</a>
<a class="abs nav-link" style="left:969px">BLOG</a>
<div class="abs brand-dome"></div>
<div class="abs brand-dot"></div>
<div class="abs brand">velmora bridal co.</div>

<!-- hero -->
<div class="abs photo hero" role="img" aria-label="Couple embracing on a grassy clifftop above a curving turquoise beach"></div>
<h1 class="abs hero-title">Services</h1>
<svg class="abs arrow" style="left:40px" width="20" height="40" viewBox="0 0 20 40"><path d="M16 4 L4 20 L16 36" fill="none" stroke="rgba(255,255,255,.6)" stroke-width="2"/></svg>
<svg class="abs arrow" style="left:1138px" width="20" height="40" viewBox="0 0 20 40"><path d="M4 4 L16 20 L4 36" fill="none" stroke="rgba(255,255,255,.6)" stroke-width="2"/></svg>

<!-- elopement -->
<section>
<div class="abs service s-elope" role="img" aria-label="Couple kissing in the shallow surf at sunset on a rocky beach"></div>
<h2 class="abs heading" style="left:624px;top:800px">Elopement</h2>
<p class="abs copy" style="left:624px;top:879px">Bigger isn’t always better. Are you traveling to Puerto Rico and want to be married? Are you starting to plan a traditional wedding at home, and it’s just becoming too much? Have you already had the ‘big wedding’ and are looking for something entirely different this time around? Have you always dreamed of being married, simply and sweetly, with your feet in the sand?</p>
<a class="abs btn" style="left:624px;top:1093px">FIND OUT MORE</a>
</section>

<!-- barefoot -->
<section>
<div class="abs service s-beach" role="img" aria-label="Beach ceremony setup with white chairs and a draped wooden arch by the sea"></div>
<div class="abs s-beach-sand"></div>
<h2 class="abs heading" style="left:105px;top:1354px">Barefoot on the Beach</h2>
<p class="abs copy" style="left:105px;top:1433px;width:480px">Have you always dreamed of a beautiful wedding ceremony on a deserted tropical beach at sunset? Have you started contacting vendors, and aren’t able to get the answers or responses you need? Are you looking for a Puerto Rico beach wedding package for your ceremony but don’t really know where to start?</p>
<a class="abs btn" style="left:105px;top:1625px">FIND OUT MORE</a>
</section>

<!-- vow renewals -->
<section>
<div class="abs service s-vow" role="img" aria-label="Older couple embracing with a bright bouquet on a colorful colonial street"></div>
<h2 class="abs heading" style="left:624px;top:1912px">Vow Renewals</h2>
<p class="abs copy" style="left:624px;top:1990px">Are you taking a romantic trip to Puerto Rico for your anniversary? Would you like your family vacation to our enchanted island include a celebration of the love that brought you all together? Was your wedding a simple affair, and you’re looking for more of a ‘wedding experience’ on a beautiful beach, with photos and perhaps video?</p>
<a class="abs btn" style="left:624px;top:2183px">FIND OUT MORE</a>
</section>

<!-- cruise -->
<section>
<div class="abs service s-cruise" role="img" aria-label="Aerial view of a cruise ship sailing past a historic coastal fortress"></div>
<h2 class="abs heading" style="left:105px;top:2423px">Cruise Ship Passengers</h2>
<p class="abs copy" style="left:105px;top:2500px;width:490px">Are you planning a honeymoon cruise that departs from San Juan, and want to get married on our beautiful island? Is your cruise stopping in Puerto Rico for the day, and you’d like to elope on your shore excursion? Would you like to be legally married in Puerto Rico instead of symbolically married on your cruise ship? Are you interested in surprising your spouse by renewing your vows on a luxury boat tour of Old San Juan?</p>
<a class="abs btn" style="left:105px;top:2749px">FIND OUT MORE</a>
</section>

<!-- additional -->
<section>
<div class="abs service s-extra" role="img" aria-label="Newlyweds riding a golf cart across a sunlit lawn"></div>
<h2 class="abs heading" style="left:624px;top:3021px">Additional Services</h2>
<p class="abs copy" style="left:624px;top:3099px">Are you taking a romantic trip to Puerto Rico for your anniversary? Would you like your family vacation to our enchanted island include a celebration of the love that brought you all together? Was your wedding a simple affair, and you’re looking for more of a ‘wedding experience’ on a beautiful beach, with photos and perhaps video?</p>
<a class="abs btn" style="left:624px;top:3292px">FIND OUT MORE</a>
</section>

<!-- footer -->
<footer>
<div class="abs foot-dot"></div>
<div class="abs foot-brand">velmora bridal co.</div>
<div class="abs search">
  <div class="search-field">
    <svg class="abs" style="left:12px;top:13px" width="17" height="17" viewBox="0 0 17 17"><circle cx="7" cy="7" r="5.5" fill="none" stroke="#aaa" stroke-width="1.6"/><path d="M11 11 L15.5 15.5" stroke="#aaa" stroke-width="1.8"/></svg>
  </div>
  <div class="search-btn">SEARCH</div>
</div>

<h3 class="abs foot-heading" style="left:450px;top:3532px">About</h3>
<p class="abs foot-copy" style="left:450px;top:3576px">Velmora Bridal Co., Inc. is owned and operated by Dana Whitfield, a non-denominational minister who became ordained to perform weddings, and has extensive experience planning and coordinating hundreds of weddings on our enchanted island. She will be your point of contact at every step.</p>

<h3 class="abs foot-heading" style="left:853px;top:3532px">Contact</h3>
<div class="abs contact-row" style="left:853px;top:3584px">
  <svg width="14" height="14" viewBox="0 0 14 14"><path d="M3 1 L5.5 1 L6.5 4 L5 5.5 C6 7.5 7 8.5 8.5 9 L10 7.5 L13 8.5 L13 11 C13 12 12 13 11 13 C6 12.5 1.5 8 1 3 C1 2 2 1 3 1Z" fill="var(--gold)"/></svg>
  <span>555.014.2290</span>
</div>
<div class="abs contact-row" style="left:853px;top:3639px">
  <svg width="15" height="12" viewBox="0 0 15 12"><rect x="0.5" y="0.5" width="14" height="11" rx="1" fill="var(--gold)"/><path d="M1 1.5 L7.5 7 L14 1.5" fill="none" stroke="#fff" stroke-width="1.2"/></svg>
  <span>info@velmorabridalco.com</span>
</div>

<div class="abs rule"></div>
<p class="abs copyright">© 2020, Velmora Bridal Co.</p>
<div class="abs social" style="left:964px"></div>
<div class="abs social" style="left:997px"></div>
<div class="abs social" style="left:1030px"></div>
<div class="abs social" style="left:1063px"></div>
</footer>

</body>
</html>
```